Property investment company needs a letterhead design!

We are a new residential and commercial property investment company. Name of the company is Morvesta Group, LLC. We have a new logo and now we need letterhead! We prefer to have a professional and upscale appearance. We don't have any fixed requirements, so be creative! Thank you for considering this project. We are so excited to see what happens!

Target Market(s)

Professional

Industry/Entity Type

Real Estate Development

```html
<!DOCTYPE html>
<html lang="en">
<head>
<meta charset="utf-8">
<title>Morvesta Group, LLC — Letterhead</title>
<link href="https://fonts.googleapis.com/css2?family=Open+Sans:wght@400;600;700&family=Great+Vibes&display=swap" rel="stylesheet">
<style>
  :root {
    --backdrop: #ebebed;
    --paper: #ffffff;
    --navy: #0f2440;
    --accent: #00aeef;
    --rule: #c8c8c8;
    --ink: #1f1f1f;
    --ink-soft: #333333;
  }
  * { margin: 0; padding: 0; box-sizing: border-box; }
  html, body {
    width: 1200px; height: 1200px; overflow: hidden;
    background: var(--backdrop);
    font-family: "Open Sans", Arial, sans-serif;
    color: var(--ink);
  }
  .letterhead {
    position: absolute; left: 220px; top: 67px;
    width: 760px; height: 1066px;
    background: var(--paper);
    box-shadow: 0 2px 10px rgba(0,0,0,0.08);
  }
  .brand {
    position: absolute; left: 98px; top: 72px;
    display: flex; align-items: center; gap: 10px;
  }
  .brand-dot {
    width: 14px; height: 14px; border-radius: 50%;
    background: var(--navy);
  }
  .brand-name {
    font-weight: 700; font-size: 21px; color: var(--navy);
    letter-spacing: 0.5px; line-height: 1.15;
  }
  .rule {
    position: absolute; left: 98px; width: 564px; height: 2px;
    background: var(--rule);
  }
  .rule::before {
    content: ""; position: absolute; left: 0; top: 0;
    width: 53px; height: 2px; background: var(--accent);
  }
  .rule-top { top: 163px; }
  .rule-bottom { top: 950px; }
  .sender { position: absolute; left: 98px; top: 230px; }
  .sender-name { font-size: 14px; font-weight: 600; color: var(--accent); line-height: 18px; }
  .sender-role { font-size: 9.5px; color: var(--ink-soft); line-height: 14px; margin-bottom: 4px; }
  .sender-line { font-size: 11.5px; line-height: 18.6px; color: var(--ink); }
  .sender-line .label { display: inline-block; width: 23px; font-weight: 700; }
  .label-accent { color: var(--accent); }
  .letter-date {
    position: absolute; right: 103px; top: 349px;
    font-size: 11.5px; line-height: 18px;
  }
  .letter-body {
    position: absolute; left: 98px; top: 403px; width: 570px;
    font-size: 11.5px; line-height: 24.4px; white-space: nowrap;
  }
  .letter-body p { margin-bottom: 24.4px; }
  .letter-body span { display: block; }
  .sign-off { position: absolute; left: 98px; top: 770px; }
  .signature {
    font-family: "Great Vibes", cursive; font-size: 31px;
    color: var(--ink); line-height: 40px;
  }
  .signer-name { font-size: 12px; font-weight: 700; line-height: 14px; }
  .signer-role { font-size: 11.5px; line-height: 14px; color: var(--ink-soft); }
  .footer-contact {
    position: absolute; top: 972px;
    display: flex; align-items: center; gap: 10px;
    font-size: 11.5px; line-height: 14px; color: var(--ink);
  }
  .footer-contact svg { flex: none; }
  .contact-phone { left: 107px; }
  .contact-mail { left: 276px; }
  .contact-place { left: 489px; }
  .band {
    position: absolute; left: 0; bottom: 0; width: 100%; height: 32px;
    background: var(--accent);
  }
</style>
</head>
<body>
  <main class="letterhead">
    <div class="brand">
      <span class="brand-dot"></span>
      <span class="brand-name">Morvesta Group, LLC</span>
    </div>
    <div class="rule rule-top"></div>

    <section class="sender">
      <div class="sender-name">Daniel Harrow</div>
      <div class="sender-role">Chief Director</div>
      <div class="sender-line"><span class="label label-accent">A :</span>45-1,Lorem Road State - 8989</div>
      <div class="sender-line"><span class="label">W :</span>email@mailid.com, www.myweb.com</div>
      <div class="sender-line"><span class="label label-accent">P :</span>+880 - 12345 - 6789</div>
    </section>

    <div class="letter-date">Date, 06 May, 2021</div>

    <article class="letter-body">
      <p>
        <span>This is a sample letter that has been placed to demonstrate typing remat (Your Company). letterhead</span>
        <span>design. When positioned properly, it will serve to work in harmony with all other elements letterhead.</span>
        <span>This letterhead design is meant to project an image</span>
      </p>
      <p>
        <span>This letterhead design is meant project an image of professionalism reliability. By using simple aligen</span>
        <span>we have created a very spacious feeling. The simplicity suggest &nbsp;rengththe spaciousnes contributes h</span>
        <span>aesthetics the layout. These basic qualities along with the (Your Company)</span>
      </p>
      <p>
        <span>look and helps reinforce the (Your Company) brand. letterhead design is meant to project an image p</span>
        <span>design. When positioned properly, it will serve to work in harmony all the other elements letterhead.</span>
        <span>sionalism and reliability.</span>
      </p>
      <p>
        <span>This letterhead design is based on the (Form of your logo) form (Your Company) logo. Each stationery</span>
        <span>we have created a very spacious feeling. The simplicity suggests strength the spaciousnes contribute</span>
        <span>part of the (Form of your logo).</span>
      </p>
    </article>

    <section class="sign-off">
      <div class="signature">Daniel Harrow</div>
      <div class="signer-name">Daniel Harrow</div>
      <div class="signer-role">Manager</div>
    </section>

    <div class="rule rule-bottom"></div>

    <div class="footer-contact contact-phone">
      <svg width="22" height="34" viewBox="0 0 22 34" fill="none" stroke="var(--accent)" stroke-width="1.6">
        <rect x="1" y="1" width="20" height="32" rx="3"/>
        <line x1="1" y1="6" x2="21" y2="6"/>
        <line x1="1" y1="27" x2="21" y2="27"/>
        <line x1="8" y1="30" x2="14" y2="30"/>
      </svg>
      <span>(907) 555-0142</span>
    </div>

    <div class="footer-contact contact-mail">
      <svg width="28" height="22" viewBox="0 0 28 22" fill="none" stroke="var(--accent)" stroke-width="1.6">
        <rect x="1" y="1" width="26" height="20" rx="1.5"/>
        <polyline points="1,2 14,13 27,2"/>
        <line x1="1" y1="20" x2="11" y2="11"/>
        <line x1="27" y1="20" x2="17" y2="11"/>
      </svg>
      <span>MorvestaLLC@mailnest.com<br>www.MorvestaLLC.com</span>
    </div>

    <div class="footer-contact contact-place">
      <svg width="26" height="34" viewBox="0 0 26 34" fill="none" stroke="var(--accent)" stroke-width="1.6">
        <path d="M13 33 C13 33 1.5 20 1.5 12.5 A11.5 11.5 0 0 1 24.5 12.5 C24.5 20 13 33 13 33 Z"/>
        <circle cx="13" cy="12.5" r="5"/>
      </svg>
      <span>1184 N. Alder Ave.<br>Pine Hollow, MI 49012</span>
    </div>

    <div class="band"></div>
  </main>
</body>
</html>
```